Criação de Peça Gráfica (unidade) para Logística, Entrega & Armazenamento
A empresa queria:
" Transporte Geral de Cargas, seja rodoviário, rodo-fluvial e maritímo. Também somos Agentes/Representantes Internacioais "

```html
<!DOCTYPE html>
<html lang="pt-BR">
<head>
<meta charset="utf-8">
<title>Segurança de sua carga</title>
<link rel="stylesheet" href="https://fonts.googleapis.com/css2?family=Arimo:wght@400;700&display=swap">
<style>
  :root {
    --page-bg: #ececec;
    --card-bg: #ffffff;
    --brand-red: #a3202a;
    --brand-red-deep: #8c1821;
    --text-dark: #2b2b2b;
    --text-mid: #4a4a4a;
    --photo-light: #c9d3dc;
    --photo-mid: #7f8fa0;
    --photo-dark: #3c4a58;
  }
  * { box-sizing: border-box; margin: 0; padding: 0; }
  html, body { width: 1200px; height: 1200px; overflow: hidden; }
  body {
    background: var(--page-bg);
    font-family: "Arimo", Arial, sans-serif;
    color: var(--text-dark);
    position: relative;
  }
  .flyer {
    position: absolute;
    left: 100px;
    top: 289px;
    width: 1000px;
    height: 622px;
    background: var(--card-bg);
    overflow: hidden;
  }
  .flyer-art { position: absolute; inset: 0; }
  .headline-box {
    position: absolute;
    left: 32px;
    top: 252px;
    width: 372px;
    height: 164px;
    background: var(--brand-red);
    opacity: 0.93;
    color: #fff;
    padding: 42px 0 0 44px;
    text-transform: uppercase;
    font-weight: 700;
    line-height: 1.05;
  }
  .headline-box .line-small { font-size: 30px; letter-spacing: 0.5px; }
  .headline-box .line-large { font-size: 40px; }
  .brand {
    position: absolute;
    right: 36px;
    top: 42px;
    width: 110px;
    text-align: center;
  }
  .brand-dot {
    width: 52px; height: 52px; border-radius: 50%;
    background: var(--brand-red-deep);
    margin: 0 auto 6px;
  }
  .brand-name { font-size: 14px; font-weight: 700; color: var(--brand-red-deep); letter-spacing: 0.5px; }
  .brand-tag { font-size: 8px; color: var(--text-mid); margin-top: 3px; line-height: 1.2; }
  .features {
    position: absolute;
    left: 540px;
    top: 172px;
    width: 360px;
    list-style: none;
    font-size: 16px;
    line-height: 1.35;
    color: var(--text-mid);
  }
  .features li { position: relative; padding-left: 36px; margin-bottom: 20px; }
  .features li.check::before {
    content: "✓";
    position: absolute; left: 0; top: 0;
    color: var(--text-dark);
    font-size: 15px;
  }
  .features li.dot { margin-top: 38px; }
  .features li.dot::before {
    content: "";
    position: absolute; left: 0; top: 7px;
    width: 6px; height: 6px; border-radius: 50%;
    background: var(--text-dark);
  }
</style>
</head>
<body>
  <section class="flyer">
    <svg class="flyer-art" viewBox="0 0 1000 622" width="1000" height="622">
      <defs>
        <linearGradient id="photoTone" x1="0" y1="0" x2="1" y2="1">
          <stop offset="0" stop-color="var(--photo-light)"/>
          <stop offset="0.55" stop-color="var(--photo-mid)"/>
          <stop offset="1" stop-color="var(--photo-dark)"/>
        </linearGradient>
        <radialGradient id="skyTone" cx="0.6" cy="0.35" r="0.6">
          <stop offset="0" stop-color="#dfe3e7"/>
          <stop offset="1" stop-color="#ffffff"/>
        </radialGradient>
      </defs>
      <rect x="400" y="0" width="600" height="622" fill="url(#skyTone)" opacity="0.7" role="img" aria-label="Faint background image of an airplane in the sky"/>
      <path d="M0 0 H390 C480 150 500 400 363 622 H0 Z" fill="url(#photoTone)" role="img" aria-label="Photo of a businessman using a phone and laptop with a cargo truck and network icons"/>
      <path d="M390 0 C480 150 500 400 363 622" fill="none" stroke="var(--brand-red)" stroke-width="6"/>
    </svg>

    <div class="headline-box">
      <div class="line-small">Segurança de</div>
      <div class="line-large">Sua Carga</div>
    </div>

    <div class="brand">
      <div class="brand-dot"></div>
      <div class="brand-name">NORTIVA LOG</div>
      <div class="brand-tag">Transporte e Logística Internacional</div>
    </div>

    <ul class="features">
      <li class="check">Apólice de seguros;</li>
      <li class="check">Rastreamento e Gerenciamento de risco;</li>
      <li class="check">Sistema de Automação<br>Comercial e de Transportes.</li>
      <li class="dot">Informativos da movimentação da sua carga desde a coleta até a entrega, através de informativos enviado, automaticamente, por e-mail;</li>
      <li class="dot">Acesso nosso site, www.nortivalog.com.br de posse de login e senha, enviados por e-mail, você poderá acompanhar sua carga.</li>
    </ul>
  </section>
</body>
</html>
```